New Architectural Firm Business Cards

New Business card to compliment previous pixel forum logo (attached). Please design a business card that is simple, modern, creative....please do not use "symbols", simply the logo and associated graphics/text. The front should contain name/address/phone/email/web address (with graphics).....back should be 100% graphic design using the logo somehow. Hoping for a two color (black and yellow) design. full bleed design, no borders

Target Market(s)

Commercial Architecture Clients

Industry/Entity Type

Architecture

Contact Information for Business Card

Please design a business card that is simple, modern, creative....please do not use "symbols", simply the logo and associated graphics/text. The front should contain name/address/phone/email/web address (with graphics).....back should be 100% graphic design using the logo somehow

Font styles to use
Sans Serif

Colors
FFF300
FFF600
FEFA6F
FFFEC7
FFFEE8

Requirements
Must have
• Clean, Modern Design
Should not have
• Stock images or "icons"

```html
<!DOCTYPE html>
<html lang="en">
<head>
<meta charset="utf-8">
<title>Kestrel Architecture – Business Card</title>
<link href="https://fonts.googleapis.com/css2?family=Montserrat:wght@500;600;700&family=Roboto+Condensed:wght@700&display=swap" rel="stylesheet">
<style>
  :root {
    --paper: #ffffff;
    --card: #000000;
    --accent: #f6c416;
    --ink: #ffffff;
  }
  * { margin: 0; padding: 0; box-sizing: border-box; }
  html, body {
    width: 1200px;
    height: 1200px;
    overflow: hidden;
    background: var(--paper);
  }
  .sheet {
    position: relative;
    width: 1200px;
    height: 1200px;
  }
  .card {
    position: absolute;
    left: 180px;
    width: 840px;
    height: 480px;
    background: var(--card);
    overflow: hidden;
  }
  .card--back { top: 83px; }
  .card--front { top: 635px; }

  .wordmark {
    position: absolute;
    font-family: "Roboto Condensed", "Arial Narrow", sans-serif;
    font-weight: 700;
    color: var(--accent);
    text-transform: uppercase;
    line-height: 0.95;
    letter-spacing: 0.01em;
  }
  .wordmark__line { display: block; }
  .card--back .wordmark {
    left: 0;
    right: 0;
    top: 150px;
    text-align: center;
    font-size: 76px;
  }
  .card--front .wordmark {
    left: 70px;
    top: 168px;
    font-size: 56px;
  }

  .contact {
    position: absolute;
    right: 70px;
    top: 52px;
    text-align: right;
    font-family: "Montserrat", sans-serif;
    color: var(--ink);
  }
  .contact__name {
    font-size: 29px;
    font-weight: 700;
    letter-spacing: 0.04em;
    line-height: 1;
  }
  .contact__role {
    margin-top: 33px;
    font-size: 21px;
    font-weight: 600;
    line-height: 1;
  }
  .contact__phone {
    margin-top: 41px;
    font-size: 29px;
    font-weight: 600;
    letter-spacing: 0.04em;
    line-height: 1;
  }
  .contact__web {
    margin-top: 40px;
    font-size: 21px;
    font-weight: 500;
    line-height: 38px;
    letter-spacing: 0.02em;
  }
  .contact__address {
    margin-top: 9px;
    font-size: 21px;
    font-weight: 500;
    line-height: 38px;
    letter-spacing: 0.03em;
    font-style: normal;
  }

  .accent-rule {
    position: absolute;
    right: 0;
    background: var(--accent);
  }
  .accent-rule--short { top: 98px; width: 48px; height: 6px; }
  .accent-rule--tall { top: 270px; width: 10px; height: 142px; }
</style>
</head>
<body>
  <main class="sheet">
    <section class="card card--back" aria-label="Card back">
      <div class="wordmark">
        <span class="wordmark__line">Kestrel</span>
        <span class="wordmark__line">Architecture</span>
      </div>
    </section>

    <section class="card card--front" aria-label="Card front">
      <div class="wordmark">
        <span class="wordmark__line">Kestrel</span>
        <span class="wordmark__line">Architecture</span>
      </div>

      <div class="contact">
        <p class="contact__name">ADAM RELLOW</p>
        <p class="contact__role">President</p>
        <p class="contact__phone">555.214.7780</p>
        <p class="contact__web">adamrel@kestrelarch.com<br>www.kestrelarch.com</p>
        <address class="contact__address">4815 North Harbor Street,<br>Milford Bay, ZZ 60514</address>
      </div>

      <span class="accent-rule accent-rule--short"></span>
      <span class="accent-rule accent-rule--tall"></span>
    </section>
  </main>
</body>
</html>
```